Web page design/layout for dog breeder

We are looking for a new layout/design for our current web page. Current web pages can be found at http://ruddyhound.sitefold.com.

We recently uploaded the PTR Kennel of Renown banner that we would like to have displayed on the home page.

```html
<!DOCTYPE html>
<html lang="en">
<head>
<meta charset="utf-8">
<title>Ruddyhound Vizslas — About</title>
<link href="https://fonts.googleapis.com/css2?family=Nunito+Sans:wght@400;700&display=swap" rel="stylesheet">
<style>
  :root {
    --page-bg: #ffffff;
    --ink: #111111;
    --nav-ink: #555a5a;
    --nav-active: #a8b0b0;
    --body-ink: #3d3d3d;
    --rule: #d4d4d4;
    --photo-dark: #1d1a18;
    --photo-coat: #8a4a22;
    --photo-snow: #e9ecef;
  }
  html, body {
    margin: 0;
    padding: 0;
    width: 1200px;
    height: 1048px;
    overflow: hidden;
    background: var(--page-bg);
    font-family: "Nunito Sans", sans-serif;
  }
  .page {
    position: relative;
    width: 1200px;
    height: 1048px;
  }
  .brand {
    position: absolute;
    top: 120px;
    left: 0;
    width: 1200px;
    text-align: center;
    margin: 0;
    font-size: 33px;
    font-weight: 700;
    letter-spacing: 1px;
    color: var(--ink);
    text-transform: uppercase;
  }
  .main-nav {
    position: absolute;
    top: 269px;
    left: 0;
    width: 1200px;
    display: flex;
    justify-content: center;
    gap: 31px;
    margin: 0;
    padding: 0;
    list-style: none;
  }
  .main-nav a {
    font-size: 14.5px;
    letter-spacing: 2.6px;
    text-transform: uppercase;
    text-decoration: none;
    color: var(--nav-ink);
  }
  .main-nav a.is-current {
    color: var(--nav-active);
  }
  .hero-photo {
    position: absolute;
    top: 418px;
    left: 438px;
    width: 320px;
    height: 449px;
    background:
      radial-gradient(ellipse 40% 45% at 50% 50%, var(--photo-coat) 0%, rgba(138,74,34,0.85) 55%, rgba(138,74,34,0) 100%),
      linear-gradient(180deg, var(--photo-dark) 0%, #4a4440 45%, #9aa0a6 75%, var(--photo-snow) 100%);
  }
  .about-text {
    position: absolute;
    top: 898px;
    left: 300px;
    width: 600px;
    margin: 0;
    text-align: center;
    font-size: 17px;
    line-height: 30.5px;
    color: var(--body-ink);
  }
  .page-rule {
    position: absolute;
    left: 0;
    top: 1044px;
    width: 1200px;
    height: 1px;
    background: var(--rule);
  }
</style>
</head>
<body>
<div class="page">
  <header>
    <h1 class="brand">Ruddyhound Vizslas</h1>
    <nav>
      <ul class="main-nav">
        <li><a class="is-current" href="#">About</a></li>
        <li><a href="#">Our Dogs</a></li>
        <li><a href="#">Images</a></li>
        <li><a href="#">Upcoming Litters</a></li>
        <li><a href="#">Litters</a></li>
        <li><a href="#">Contact Us</a></li>
      </ul>
    </nav>
  </header>
  <main>
    <div class="hero-photo" role="img" aria-label="Photo of a red vizsla in a collar sitting in snow among bare winter branches"></div>
    <p class="about-text">We were introduced to our first vizsla on a hunting trip in the mid 1990s.&nbsp; We were impressed by this medium sized dog that had a superior nose and high-class hunting ability. And so it began, our first vizsla, Rusty, joined our family in 1999.</p>
  </main>
  <div class="page-rule"></div>
</div>
</body>
</html>
```